Company brochure for Cedarline Stride Works, Inc.

We need a company brochure that lets referral sources know who we are, where are locations are and what services we offer. Our website is www.cedarlinestrideinc.com and we are on Facebook and Instagram. We need the brochure to feature both braces and prosthetics.

```html
<!DOCTYPE html>
<html lang="en">
<head>
<meta charset="utf-8">
<title>Cedarline Stride Works – Company Brochure</title>
<link rel="stylesheet" href="https://fonts.googleapis.com/css2?family=Montserrat:wght@600;700;800&family=Roboto:wght@400;500;700&display=swap">
<style>
:root{
  --navy:#0f3f70;
  --navy-deep:#0a2e55;
  --orange:#e85d1e;
  --ink:#2b2b2b;
  --grey-bg:#dcdcdc;
  --white:#ffffff;
  --tick:#2f6aa8;
}
*{box-sizing:border-box;margin:0;padding:0}
html,body{width:1200px;height:4000px;overflow:hidden}
body{background:var(--grey-bg);font-family:'Roboto',Arial,sans-serif;color:var(--ink)}
.spread{position:absolute;left:60px;width:1080px;height:836px;display:grid;grid-template-columns:repeat(3,360px);box-shadow:0 10px 30px rgba(0,0,0,.25)}
.spread--outside{top:1060px}
.spread--inside{top:2100px}
.panel{position:relative;overflow:hidden;background:var(--white)}
.panel__body{position:relative;z-index:2;padding:26px 24px 0}
.panel p{font-size:8.2px;line-height:1.38;text-align:justify;margin-bottom:8px}
.title-main{font-family:'Montserrat',sans-serif;font-weight:800;font-size:23px;color:var(--navy);letter-spacing:.5px;margin-bottom:12px}
.title-orange{font-family:'Roboto',sans-serif;font-weight:400;font-size:14.5px;color:var(--orange);margin:14px 0 6px}
.title-orange:first-child{margin-top:0}
.wave{position:absolute;left:0;bottom:0;width:360px;height:130px;z-index:1}

/* mission panel */
.panel--mission{background:linear-gradient(180deg,var(--navy) 0%,var(--navy-deep) 100%);color:var(--white)}
.panel--mission .panel__body{padding-top:64px}
.mission-title{font-family:'Roboto',sans-serif;font-weight:500;font-size:14.5px;text-align:center;margin-bottom:22px}
.panel--mission p{color:#e6eef7}
.contact-box{position:absolute;left:28px;right:28px;top:352px;height:288px;border:1.5px solid rgba(255,255,255,.75);border-radius:14px;display:flex;flex-direction:column;align-items:center;justify-content:space-around;padding:18px 10px;text-align:center;font-size:10.5px;line-height:1.4;background:rgba(255,255,255,.04)}
.contact-box strong{font-weight:700}
.contact-item svg{display:block;margin:0 auto 6px;width:24px;height:24px}
.site{position:absolute;left:0;right:0;bottom:16px;text-align:center;font-weight:700;font-size:12px;color:var(--white);z-index:3}

/* cover panel */
.brand{height:118px;display:flex;flex-direction:column;align-items:center;justify-content:center;gap:8px}
.brand__dot{width:34px;height:34px;border-radius:50%;background:var(--navy)}
.brand__name{font-family:'Roboto',sans-serif;font-weight:700;font-size:11.5px;color:var(--navy)}
.photo{width:100%;display:block}
.photo--lab{height:430px;background:linear-gradient(160deg,#eef3f8 0%,#c9d7e6 45%,#9fb4c9 100%)}
.cover-foot{position:absolute;left:0;top:520px;width:360px;height:316px}
.cover-foot svg{position:absolute;inset:0}
.cover-title{position:absolute;left:0;right:0;top:130px;text-align:center;font-family:'Montserrat',sans-serif;font-weight:800;color:var(--white);z-index:2;line-height:1.15}
.cover-title .lead{display:block;font-size:24px;color:var(--navy-deep)}
.cover-title .rest{display:block;font-size:18px;letter-spacing:.5px}

/* service lists */
.list-head{font-family:'Montserrat',sans-serif;font-weight:700;font-size:13.5px;color:var(--navy);margin:14px 0 6px;letter-spacing:.3px}
.list-head:first-child{margin-top:0}
.sub-head{font-size:12.5px;color:var(--orange);margin:8px 0 5px;font-weight:400;line-height:1.15}
.ticks{list-style:none;columns:2;column-gap:12px}
.ticks--three{columns:3}
.ticks--one{columns:1}
.ticks li{position:relative;padding-left:13px;font-size:8.4px;line-height:1.25;margin-bottom:4px;break-inside:avoid}
.ticks li::before{content:"";position:absolute;left:0;top:.5px;width:8px;height:8px;border:1px solid var(--tick);border-radius:50%}
.ticks li::after{content:"";position:absolute;left:2.7px;top:2.1px;width:2px;height:3.4px;border:solid var(--tick);border-width:0 1px 1px 0;transform:rotate(45deg)}
.cols{display:grid;grid-template-columns:1fr 1fr;gap:10px}
.photo--team{position:absolute;left:0;right:0;bottom:64px;height:200px;background:linear-gradient(180deg,#f3f6fa 0%,#c7d3e0 60%,#8ea6bf 100%);z-index:1}
.team-foot{position:absolute;left:0;right:0;bottom:0;height:110px;z-index:2}
</style>
</head>
<body>

<!-- OUTSIDE SPREAD -->
<section class="spread spread--outside" aria-label="Brochure outside">
  <article class="panel panel--about">
    <div class="panel__body">
      <h2 class="title-main">ABOUT US</h2>
      <p>Cedarline Stride Works has been providing quality, compassionate care to residents of St. Louis and Southern Illinois since 1983. A recognized leader in the field, our experts work as a team to create the most functional solution to your orthotic, prosthetic and pedorthic needs using the latest technology available. Our patient-centered, team approach means we work closely with your doctor, nurse, therapist and family to create custom made solutions that work for you.</p>
      <p>Our practitioners make up the largest and most experienced practice in the area. We have both adult and pediatric specialists. Our board-certified practitioners regularly attend and conduct continuing education programs and clinics allowing us to bring our patients the very latest in technology and developments in the field. Our St. Louis based Central Fabrication Facility allows us to fabricate your device with speed, quality, and convenience.</p>
      <h3 class="title-orange">Emergency 24/7 Service</h3>
      <p>Our staff is available 24 hours a day, 7 days a week for emergencies that cannot wait until the next business day. At Cedarline, we are dedicated to providing the very best patient experience.</p>
      <p>With seven patient care centers to choose from, there is one near you. Call for an appointment today.</p>
      <h3 class="title-orange">Prosthetic Services</h3>
      <p>There are approximately 2 million people living with limb loss in the United States. Most limb loss occurs in those with compromised vascular systems, frequently because of complications from diabetes. Other causes of limb loss include cancer, traumatic injuries, or congenital disorders.</p>
      <p>At Cedarline Stride Works, we understand how devastating it is to lose a limb, and we are proud to be able to help our patients regain their function and self-confidence. The loss of a limb or the birth of a child with a limb difference doesn't have to be a limitation; it could be the beginning of a powerful new life. We at Cedarline want to become part of your journey in a life without limitations. By working as a team and being a partner in the process, we can achieve your goals with a good fitting prosthesis that you need and deserve.</p>
      <p>Within our experienced team of prosthetists, we can design, fit, and fabricate a custom prostheses that is right for you.</p>
    </div>
    <svg class="wave" viewBox="0 0 360 130" preserveAspectRatio="none" aria-hidden="true">
      <path d="M0 30 C90 95 230 105 360 60 L360 130 L0 130Z" fill="var(--orange)"/>
      <path d="M0 44 C90 106 230 114 360 72 L360 130 L0 130Z" fill="var(--white)"/>
      <path d="M0 56 C90 116 230 124 360 84 L360 130 L0 130Z" fill="var(--navy)"/>
    </svg>
  </article>

  <article class="panel panel--mission">
    <div class="panel__body">
      <h2 class="mission-title">Our Mission</h2>
      <p>We are people committed to using every scientific and technical development available to restore the physical capabilities of the disabled. By combining intellectual know-how and modern technology we seek to help the "disabled" become "enabled".</p>
      <p>Our pledge is to use all of our orthotic and prosthetic resources to empower individuals with physical challenges to participate in all facets of life.</p>
    </div>
    <div class="contact-box">
      <div class="contact-item">
        <svg viewBox="0 0 24 24" aria-hidden="true"><circle cx="12" cy="12" r="12" fill="#fff"/><path d="M12 5a4.5 4.5 0 0 0-4.5 4.5C7.5 13 12 19 12 19s4.5-6 4.5-9.5A4.5 4.5 0 0 0 12 5z" fill="var(--navy)"/><circle cx="12" cy="9.5" r="1.7" fill="#fff"/></svg>
        215 BIRCHWOOD AVE.<br>KIRKFIELD, MO 63120-4410
      </div>
      <div class="contact-item">
        <svg viewBox="0 0 24 24" aria-hidden="true"><circle cx="12" cy="12" r="12" fill="#fff"/><path d="M8.6 6.5l2 2.4-1.3 1.5a8 8 0 0 0 4.3 4.3l1.5-1.3 2.4 2-1.3 2.2C12.5 17.6 6.4 11.5 6.4 7.8z" fill="var(--navy)"/></svg>
        PHONE: <strong>(314) 555-0142</strong>
      </div>
      <div class="contact-item">
        <svg viewBox="0 0 24 24" aria-hidden="true"><circle cx="12" cy="12" r="12" fill="#fff"/><rect x="8.5" y="6" width="7" height="4" fill="var(--navy)"/><rect x="6.5" y="10" width="11" height="5" rx="1" fill="var(--navy)"/><rect x="8.5" y="13.5" width="7" height="4" fill="var(--navy)" stroke="#fff" stroke-width=".8"/></svg>
        FAX: <strong>(888) 555-0187</strong>
      </div>
      <div class="contact-item">
        <svg viewBox="0 0 24 24" aria-hidden="true"><circle cx="12" cy="12" r="12" fill="#fff"/><rect x="7" y="7.5" width="10" height="10" rx="1" fill="var(--navy)"/><rect x="8.3" y="10.5" width="7.4" height="5.7" fill="#fff"/><rect x="9" y="6" width="1.2" height="3" fill="var(--navy)"/><rect x="13.8" y="6" width="1.2" height="3" fill="var(--navy)"/></svg>
        MONDAY THROUGH FRIDAY -<br><strong>8:30 AM TO 4:30 PM</strong>
      </div>
    </div>
    <p class="site">www.cedarlinestrideinc.com</p>
  </article>

  <article class="panel panel--cover">
    <div class="brand">
      <span class="brand__dot" aria-hidden="true"></span>
      <span class="brand__name">Cedarline Stride Works, Inc.</span>
    </div>
    <div class="photo photo--lab" role="img" aria-label="Photo of a laboratory bench with a microscope and glass flasks"></div>
    <div class="cover-foot">
      <svg viewBox="0 0 360 316" preserveAspectRatio="none" aria-hidden="true">
        <path d="M0 60 C110 0 250 -10 360 30 L360 316 L0 316Z" fill="var(--orange)"/>
        <path d="M0 74 C110 14 250 4 360 44 L360 316 L0 316Z" fill="var(--white)"/>
        <path d="M0 160 L360 160 L360 316 L0 316Z" fill="var(--navy)"/>
      </svg>
      <h1 class="cover-title"><span class="lead">WELCOME TO</span><span class="rest">CEDARLINE STRIDE<br>WORKS</span></h1>
    </div>
    <p class="site">www.cedarlinestrideinc.com</p>
  </article>
</section>

<!-- INSIDE SPREAD -->
<section class="spread spread--inside" aria-label="Brochure inside">
  <article class="panel">
    <div class="panel__body">
      <h3 class="title-orange">Orthotic Services</h3>
      <p>After receiving a prescription from your physician for an orthopedic brace, you will most likely be referred to an orthotist, orthotic company or clinic team. An Orthotist is a trained healthcare professional who specializes in making a wide range of custom fit braces. It is the orthotists job to cast, measure, build, fit, maintain, and educate you on the proper wear and care of your brace. Often your physician will make the referral to a clinic team. Orthotic clinical teams for children are especially important because of changes in growth and development. This team is made up of the physician, nurse, orthotist and therapist all working together to achieve the best possible outcome. Remember the most important member and contributor to the team is YOU.</p>
      <p>The goal of orthotic bracing is different for each patient. The goals could involve increasing your mobility, decrease a hospital stay, supporting a week or deformed limb, reducing fatigue, picking up you toe as you walk, stopping the progression of a spinal curve, maintain correction of a foot, protecting a new surgery or fixing a flat spot on a child's head. Whatever the problem area is, our orthotists are experts in wide variety bracing solutions.</p>
      <p>Cedarline Stride Works in St. Louis | NCPA Accredited</p>
      <p>At Cedarline Stride Works, our facilities are NCPA accredited and our orthotic staff is made up of certified professionals. We have both adult and pediatric specialists, so you can be sure that the right orthotist is a member of your team.</p>
      <h3 class="title-orange" style="margin-top:30px">NCPA Accredited Facility</h3>
      <p>Did you know that in most states there are no requirements for education, certification or licensure for orthotists, prosthetists or pedorthists? Take a proactive approach in determining who you will be working with - being informed will only help you gain a positive outcome. It's important that you choose a highly qualified, rigorously trained individual, someone who has the appropriate education and training and is NCPA certified in their discipline. Choosing an NCPA accredited facility is also just as important. NCPA's exacting standards ensure that NCPA accredited facilities have earned the mark of exceptional quality and superior patient care. You deserve nothing less.</p>
      <p>Cedarline Stride Works is an NCPA Certified Facility staffed with NCPA certified professional who can help you reach your goals. Certification and accreditation provides you with the assurance that the right practitioner is a member of your team.</p>
    </div>
    <svg class="wave" viewBox="0 0 360 130" preserveAspectRatio="none" aria-hidden="true">
      <path d="M0 30 C90 95 230 105 360 60 L360 130 L0 130Z" fill="var(--orange)"/>
      <path d="M0 44 C90 106 230 114 360 72 L360 130 L0 130Z" fill="var(--white)"/>
      <path d="M0 56 C90 116 230 124 360 84 L360 130 L0 130Z" fill="var(--navy)"/>
    </svg>
  </article>

  <article class="panel">
    <div class="panel__body">
      <h3 class="list-head">CRANIAL</h3>
      <ul class="ticks ticks--three">
        <li>Cranial Remolding Orthoses</li><li>Custom Post-Surgical Helmets</li><li>Protective Helmets</li>
      </ul>
      <h3 class="list-head" style="margin-top:20px">CERVICAL</h3>
      <ul class="ticks">
        <li>Wire Foam Collar</li><li>Molded Plastic Collar</li><li>Semi Rigid Collar</li><li>SOMI</li>
        <li>Rigid Support Collars</li><li>HALO</li><li>Non Invasive Halo</li><li>Torticollis Orthoses</li>
      </ul>
      <h3 class="list-head" style="margin-top:20px">LOWER EXTREMITY ORTHOSIS</h3>
      <h4 class="sub-head">Foot Orthotics</h4>
      <ul class="ticks"><li>Foot Orthoses</li><li>UCBL Orthoses</li></ul>
      <h4 class="sub-head" style="margin-top:14px">Ankle Foot Orthoses (AFO)</h4>
      <ul class="ticks">
        <li>Ankle Supports</li><li>Prefabricated AFO's</li><li>Total Carbon Fiber AFO's</li><li>Solid Ankle AFO's</li><li>Posterior Leaf Spring AFO's</li><li>Metal Double Upright AFO's</li><li>Ground Reaction AFO's</li><li>Spiral Carbon Fiber AFO's</li>
        <li>CAM Walker</li><li>Pressure Relief AFO</li><li>Tibial Fracture Brace</li><li>Tibial Torsion Orthosis</li><li>Dynamic ROM AFO</li><li>Plantar Fasciitis Splint</li><li>Charcot Restraint Walker</li><li>Lace-Up Gauntlet AFO</li>
      </ul>
      <h4 class="sub-head" style="margin-top:14px">Knee Ankle Foot Orthoses</h4>
      <ul class="ticks">
        <li>Knee Patella Supports</li><li>Knee Immobilizers</li><li>ROM Knee Braces</li><li>Single Upright KAFO's</li><li>Double Upright KAFO's</li>
        <li>Femoral Fracture Braces</li><li>ACL / PCL Knee Braces</li><li>OA Knee Braces</li><li>Hyperextension KO</li><li>Dynamic ROM KAFO / KO's</li>
      </ul>
      <div class="cols" style="margin-top:12px">
        <div>
          <h4 class="sub-head">Hip Knee Ankle Foot</h4>
          <ul class="ticks ticks--one">
            <li>HKAFO Femoral Fx Brace</li><li>Custom HKAFO</li><li>Reciprocating Gait Orthoses</li><li>Standing Frame</li><li>A-Frame</li><li>Parapodium</li>
          </ul>
        </div>
        <div>
          <h4 class="sub-head">Hip Orthoses</h4>
          <ul class="ticks ticks--one">
            <li>Adjustable Hip Abduction</li><li>Infant Hip Harness</li><li>Hip Abduction Braces</li><li>Static Hip Abduction Braces</li><li>Ambulatory Hip Orthosis</li><li>Sitting Walking Hip Orthosis</li><li>Dynamic Hip Abduction</li>
          </ul>
        </div>
      </div>
    </div>
  </article>

  <article class="panel">
    <div class="panel__body">
      <h3 class="list-head">UPPER EXTREMITY</h3>
      <div class="cols">
        <div>
          <h4 class="sub-head">Wrist Hand<br>Orthoses</h4>
          <ul class="ticks ticks--one">
            <li>Wrist Cock Up</li><li>Resting Hand Splint</li><li>Custom Molded WHO</li><li>Dynamic Finger Splint</li><li>Dynamic Hand Finger Splint</li><li>Dynamic Wrist Hand Finger Splint</li><li>Tenodesis Splint</li><li>Dynamic Range of Motion WHO</li>
          </ul>
        </div>
        <div>
          <h4 class="sub-head">Shoulder-Elbow<br>Orthoses</h4>
          <ul class="ticks ticks--one">
            <li>Shoulder Abduction Harness</li><li>Clavicle Sling</li><li>Static Elbow Orthoses</li><li>Articulating Elbow Orthoses</li><li>Dynamic Range of Motion Elbow</li><li>Ulnar Fracture Orthoses</li><li>Humeral Fracture Orthose</li>
          </ul>
        </div>
      </div>
      <h4 class="sub-head" style="margin-top:12px">Pediatric Corrective</h4>
      <ul class="ticks">
        <li>Straight Last Shoes</li><li>Clubfoot Abduction Bars</li><li>Foot Abduction Splints</li>
        <li>Crawling Support Bars</li><li>Elbow Extension Brace</li>
      </ul>
      <h3 class="list-head" style="margin-top:16px">SPINAL</h3>
      <div class="cols">
        <div>
          <h4 class="sub-head">Spinal/Thoracic</h4>
          <ul class="ticks ticks--one">
            <li>LS Corset</li><li>Chairback LSO</li><li>Custom Molded LSO</li><li>Hyperextension TLSO</li><li>TLSO Corset</li><li>Custom Molded TLSO</li>
          </ul>
        </div>
        <div>
          <h4 class="sub-head">Spine/Scoliosis</h4>
          <ul class="ticks ticks--one">
            <li>Scoliosis TLSO</li><li>Cervico-Thoracic CTLSO</li>
          </ul>
        </div>
      </div>
    </div>
    <div class="photo--team" role="img" aria-label="Group photo of the clinical staff in lab coats and scrubs"></div>
    <svg class="team-foot" viewBox="0 0 360 110" preserveAspectRatio="none" aria-hidden="true">
      <path d="M0 40 C120 10 250 10 360 30 L360 110 L0 110Z" fill="var(--navy)"/>
    </svg>
    <p class="site">www.cedarlinestrideinc.com</p>
  </article>
</section>

</body>
</html>
```